Marketing Services Flyer

We need a flyer for a new company based in Annapolis, MD called Tidewell Messaging. We offer Social Media Management, Traditional Media Ad Design/Placement, Professional Video Production, Email Marketing and Graphic Design services. This flyer will serve as a leave behind/sales flyer to promote our services. I have attached the logo. The font in the logo is Helvetica Neue Light STD.

Tag line:

Tidewell Messaging
Strategic Marketing and Integrated Communications
Updates

I need another section added under the services I offer.  Please add this in along with the others. 

Custom Content

• Blogging - We will develop a strategy, write your blog and promote it via social media
• Press Releases - We will write press releases about exciting developments in your business and get them posted in places where reporters will actually see them. 
• Reviews - We will gather and post reviews of your business from your customers 

Target Market(s)

This is targeted to business owners who are too busy to do their own online marketing.

Industry/Entity Type

Graphic Design

Requirements
Must have
• I would like this flyer to have a front and back page so that I may print a double sided flyer. I have a logo that will need to be included. I want to illustrate the services I can provide with pictures and text. For example, for Social Media Management I would like the logo for Chirpnet, Friendly, Orbix +, Spots, Workloop, etc.

I have attached pictures of local lifestyle magazines that I would like used to illustrate my Traditional Media Ad services. Please use these images or other images of the same publications if you find better ones.

I will provide copy in an attachment.

Must include contact information and Social Media addresses.

Chirpnet.com/TidewellMsg
Friendly.com/TWMsg
Clipstream.com/TidewellMsg

phone - 410.555.0148
email - info@tidewellmessaging.com
Nice to have
• A screwpile lighthouse is a type of lighthouse found on Chesapeake Bay. If it works it would be nice to incorporate images of these somehow, if it does not work that is fine.

Include this copy in an eye catching way:

Social - Email - INTEGRATED - Video - Design

I have a background vector image file I will attach to this. I bought it so if you think it would add to the design then use it, or use part of it. If you don't think it adds to the design then leave it off, up to you.

```html
<!DOCTYPE html>
<html lang="en">
<head>
<meta charset="utf-8">
<title>Tidewell Messaging – Strategic Marketing &amp; Integrated Communications</title>
<link href="https://fonts.googleapis.com/css2?family=Arimo:wght@400&family=Roboto+Condensed:wght@300;400;700;800&display=swap" rel="stylesheet">
<style>
  :root {
    --brand-blue: #0b70b4;
    --ampersand-blue: #0a5a94;
    --band-yellow: #fecb0a;
    --ink: #1a1a1a;
    --white: #ffffff;
    --logo-grey: #8a8d90;
    --contact-grey: #444444;
  }
  * { margin: 0; padding: 0; box-sizing: border-box; }
  html, body { width: 927px; height: 1200px; overflow: hidden; background: var(--white); }
  .flyer {
    position: relative;
    width: 927px;
    height: 1200px;
    background: var(--white);
    overflow: hidden;
  }
  .hero {
    position: absolute;
    left: 0; top: 0;
    width: 927px; height: 856px;
    background: var(--brand-blue);
  }
  .hero-pointer {
    position: absolute;
    left: 433px; top: 855px;
    width: 60px; height: 36px;
  }
  .service-band {
    position: absolute;
    left: 0; top: 132px;
    width: 927px; height: 53px;
    background: var(--band-yellow);
    display: flex; align-items: center; justify-content: center;
    font-family: "Arimo", Arial, sans-serif;
    font-size: 30px;
    color: var(--ink);
    letter-spacing: 0.2px;
  }
  .headline {
    position: absolute;
    left: 0; top: 0;
    width: 927px;
    font-family: "Roboto Condensed", "Arial Narrow", sans-serif;
    color: var(--white);
    text-align: center;
  }
  .headline-ampersand {
    position: absolute;
    left: 0; top: 330px;
    width: 927px;
    text-align: center;
    font-family: "Roboto Condensed", "Arial Narrow", sans-serif;
    font-weight: 800;
    font-size: 300px;
    line-height: 1;
    color: var(--ampersand-blue);
  }
  .headline-lead {
    position: absolute;
    left: 0; top: 347px;
    width: 927px;
    font-size: 70px;
    line-height: 1;
    letter-spacing: -1px;
    text-shadow: 0 2px 3px rgba(0,0,0,0.35);
  }
  .headline-lead strong { font-weight: 700; letter-spacing: -2px; }
  .headline-lead span { font-weight: 400; }
  .headline-main {
    position: absolute;
    left: 0; top: 548px;
    width: 927px;
    font-weight: 700;
    font-size: 156px;
    line-height: 1;
    letter-spacing: -3px;
    background: linear-gradient(180deg, #ffffff 45%, #c9cdd2 100%);
    -webkit-background-clip: text;
    background-clip: text;
    color: transparent;
    filter: drop-shadow(0 4px 4px rgba(0,0,0,0.4));
  }
  .headline-tail {
    position: absolute;
    left: 0; top: 684px;
    width: 927px;
    font-weight: 400;
    font-size: 84px;
    line-height: 1;
    letter-spacing: -1px;
    text-shadow: 0 2px 3px rgba(0,0,0,0.35);
  }
  .brand-mark {
    position: absolute;
    left: 0; top: 1010px;
    width: 927px;
    display: flex; align-items: center; justify-content: center; gap: 16px;
    font-family: "Roboto Condensed", "Arial Narrow", sans-serif;
    font-weight: 300;
    font-size: 44px;
    color: var(--logo-grey);
  }
  .brand-mark-square {
    width: 26px; height: 26px;
    background: var(--logo-grey);
  }
  .contact-line {
    position: absolute;
    left: 0; top: 1148px;
    width: 927px;
    text-align: center;
    font-family: "Arimo", Arial, sans-serif;
    font-size: 20px;
    color: var(--contact-grey);
  }
</style>
</head>
<body>
  <main class="flyer">
    <section class="hero">
      <div class="service-band">Social - Email - Content - Video - Design</div>
      <div class="headline">
        <div class="headline-ampersand" aria-hidden="true">&amp;</div>
        <h1 class="headline-lead"><strong>Strategic</strong><span>MARKETING</span></h1>
        <div class="headline-main">Integrated</div>
        <div class="headline-tail">COMMUNICATIONS</div>
      </div>
    </section>
    <svg class="hero-pointer" viewBox="0 0 60 36" aria-hidden="true">
      <polygon points="0,0 60,0 30,36" fill="var(--brand-blue)"/>
    </svg>

    <div class="brand-mark">
      <span class="brand-mark-square" aria-hidden="true"></span>
      <span class="brand-mark-name">Tidewell Messaging</span>
    </div>

    <p class="contact-line">Ph: 410.555.0148 || Email: info@tidewellmessaging.com</p>
  </main>
</body>
</html>
```